ZEPHIRO needs a new business card!

ZEPHIRO is a group of gaming enthusiasts who are looking for a new corporate business card.

The typeface should be modern and minimalist with attention paid to spacing between the letters and the letters 'zephiro' look relative to each other.

Should clean, crisp and minimalist - looking serious overall but with slight tweaks to the letters to make them look playful...

Black on white is fine.

Details on the card should include:
-the word 'zephiro'
-a job title (use any, for e.g. founder)
-a name (e.g. Ned Falka)
-phone number
-email address

For inspiration: http://brisket.tumblevane-cdn.example/wp-content/uploads/2013/07/mela-1.jpg

Target Market(s)

Video gaming enthusiasts

Industry/Entity Type

Business

Requirements
Must have
• Black letter on white background.
The word "zephiro"
Nice to have
• Maybe use a conservative font like Gibraltar or Helvetica and tweaking each letter individually.

You can insert normal job titles under the "zephiro" typeface
Should not have
• Should not be cartoony or childish fonts. No colors.

```html
<!DOCTYPE html>
<html lang="en">
<head>
<meta charset="utf-8">
<title>Zephiro Business Card</title>
<link rel="stylesheet" href="https://fonts.googleapis.com/css2?family=Inter:wght@400;800&display=swap">
<style>
  :root {
    --backdrop-center: #ffffff;
    --backdrop-edge: #e6e7e8;
    --card: #ffffff;
    --card-edge: #e2e3e4;
    --ink: #353435;
    --text: #3c3c3c;
  }
  * { margin: 0; padding: 0; box-sizing: border-box; }
  html, body {
    width: 1200px;
    height: 1000px;
    overflow: hidden;
  }
  body {
    position: relative;
    background: radial-gradient(ellipse at 50% 45%, var(--backdrop-center) 0%, #f6f6f7 45%, var(--backdrop-edge) 100%);
    font-family: "Inter", "Helvetica Neue", Arial, sans-serif;
  }
  .business-card {
    position: absolute;
    left: 82px;
    top: 177px;
    width: 1038px;
    height: 648px;
    background: var(--card);
    border: 1px solid var(--card-edge);
  }
  .wordmark {
    position: absolute;
    left: 80px;
    top: 104px;
    font-weight: 800;
    font-size: 118px;
    line-height: 1;
    letter-spacing: -5px;
    color: var(--ink);
  }
  .contact {
    position: absolute;
    left: 594px;
    top: 388px;
    color: var(--text);
    font-weight: 400;
  }
  .contact-name {
    font-size: 32px;
    letter-spacing: 1px;
    line-height: 38px;
  }
  .contact-title {
    font-size: 26px;
    line-height: 34px;
  }
  .contact-details {
    margin-top: 40px;
    font-size: 26px;
    line-height: 37px;
  }
</style>
</head>
<body>
  <section class="business-card">
    <div class="wordmark">zephiro</div>
    <div class="contact">
      <p class="contact-name">NED FALKA</p>
      <p class="contact-title">Founder</p>
      <div class="contact-details">
        <p class="contact-phone">Phone : +00 000 0000</p>
        <p class="contact-email">Email: nedfalka@zephiro.example</p>
      </div>
    </div>
  </section>
</body>
</html>
```